The Wexbury Hotel Flyer

it is for a Pub that has been in the area for a long time but now we have changed the name and taken over as new owners and now have to try to get all the locals back, eating and drinking..

This Flyer is to try get all the locals to come try the new Wexbury Hotel.

We have a great new menu with daily food deals
Craft beers
Week nights Live music
Tuesday Comedy night
Sunday live music

Industry/Entity Type

Hotel

```html
<!DOCTYPE html>
<html lang="en">
<head>
<meta charset="utf-8">
<title>The Wexbury Hotel Flyer</title>
<link rel="stylesheet" href="https://fonts.googleapis.com/css2?family=Rubik:wght@500;700&family=Open+Sans:wght@600&display=swap">
<style>
  :root {
    --stage: #2b2b2b;
    --navy: #1b2a7a;
    --peach-top: #f6e2d4;
    --peach-low: #e9cfbd;
    --sky-tan: #b39a84;
    --sky-mauve: #857790;
    --sky-deep: #6e6178;
    --wood-dark: #140d09;
    --wood-mid: #3a2416;
    --wood-warm: #5a361c;
    --white: #ffffff;
    --gold: #f5a623;
    --gold-light: #f7b824;
  }
  * { margin: 0; padding: 0; box-sizing: border-box; }
  html, body {
    width: 942px; height: 1200px; overflow: hidden;
    background: var(--stage);
  }
  .flyer {
    position: absolute; left: 72px; top: 75px;
    width: 807px; height: 1043px; overflow: hidden;
    background: var(--wood-dark);
  }
  .top-band {
    position: absolute; left: 0; top: 0; width: 100%; height: 22px;
    background: var(--navy);
  }
  .top-rule {
    position: absolute; left: 0; top: 26px; width: 100%; height: 4px;
    background: var(--navy);
  }
  .header {
    position: absolute; left: 0; top: 32px; width: 100%; height: 358px;
    background: radial-gradient(ellipse 70% 60% at 50% 25%, #fbece1 0%, var(--peach-top) 45%, var(--peach-low) 100%);
  }
  .brand-name {
    position: absolute; left: 0; top: 62px; width: 100%;
    text-align: center;
    font-family: "Rubik", sans-serif; font-weight: 500;
    font-size: 60px; letter-spacing: 3px; line-height: 1;
    color: var(--navy);
  }
  .skyline {
    position: absolute; left: 0; top: 150px; width: 100%; height: 208px;
    background:
      linear-gradient(180deg,
        rgba(233,207,189,0) 0%,
        rgba(190,165,145,0.55) 22%,
        var(--sky-tan) 45%,
        #9c8a8a 68%,
        var(--sky-mauve) 86%,
        var(--sky-deep) 100%);
  }
  .wood {
    position: absolute; left: 0; top: 390px; width: 100%; height: 653px;
    background:
      radial-gradient(ellipse 60% 45% at 65% 70%, rgba(110,66,32,0.55), rgba(110,66,32,0) 70%),
      linear-gradient(180deg, var(--wood-dark) 0%, #24160e 30%, var(--wood-mid) 65%, var(--wood-warm) 100%);
  }
  .headline {
    position: absolute; left: 0; width: 100%; text-align: center;
    font-family: "Rubik", sans-serif; font-weight: 700;
    color: var(--white); line-height: 1; white-space: nowrap;
  }
  .headline-one { top: 424px; font-size: 44px; letter-spacing: 1.5px; }
  .headline-two { top: 478px; font-size: 54px; letter-spacing: 1.5px; }
  .beer-photo {
    position: absolute; left: -10px; top: 545px; width: 290px; height: 510px;
    background:
      radial-gradient(ellipse 55% 14% at 50% 6%, #f6f1ea 0%, rgba(246,241,234,0.9) 55%, rgba(246,241,234,0) 100%),
      radial-gradient(ellipse 60% 70% at 50% 50%, #f0b548 0%, #e2961f 45%, #b8701c 75%, rgba(90,54,28,0) 100%);
  }
  .food-photo {
    position: absolute; left: 330px; top: 795px; width: 477px; height: 230px;
    background: radial-gradient(ellipse 50% 45% at 55% 50%, #e0a070 0%, #b9703e 35%, #7a6a3a 60%, rgba(90,54,28,0) 100%);
  }
  .offer {
    position: absolute; left: 250px; width: 566px;
    text-align: center; white-space: nowrap;
    font-family: "Rubik", sans-serif; font-weight: 700; line-height: 1;
  }
  .offer-craft { top: 576px; font-size: 46px; color: var(--gold); }
  .offer-weeknights { top: 643px; font-size: 33px; color: var(--white); }
  .offer-comedy { top: 699px; font-size: 37px; color: var(--white); }
  .offer-sunday { top: 756px; font-size: 42px; color: var(--gold-light); }
  .web-band {
    position: absolute; left: 0; top: 957px; width: 100%; height: 48px;
    background: rgba(27,42,122,0.82);
    text-align: center;
    font-family: "Open Sans", sans-serif; font-weight: 600;
    font-size: 31px; line-height: 48px; color: var(--gold-light);
  }
</style>
</head>
<body>
  <main class="flyer">
    <div class="top-band"></div>
    <div class="top-rule"></div>

    <header class="header">
      <h1 class="brand-name">THE WEXBURY HOTEL</h1>
      <div class="skyline" role="img" aria-label="Illustrated city skyline silhouette in soft tan and mauve tones"></div>
    </header>

    <section class="wood" role="img" aria-label="Dark rustic wooden table background"></section>

    <p class="headline headline-one">WE HAVE A GREAT NEW MENU</p>
    <p class="headline headline-two">WITH DAILY FOOD DEALS</p>

    <div class="beer-photo" role="img" aria-label="Photo of two frothy pints of golden beer on a wooden barrel"></div>
    <div class="food-photo" role="img" aria-label="Photo of a toasted wrap with fresh salad"></div>

    <p class="offer offer-craft">CRAFT BEERS</p>
    <p class="offer offer-weeknights">WEEK NIGHTS LIVE MUSIC</p>
    <p class="offer offer-comedy">TUESDAY COMEDY NIGHT</p>
    <p class="offer offer-sunday">SUNDAY LIVE MUSIC</p>

    <footer class="web-band">www.thewexburyhotel.com.au</footer>
  </main>
</body>
</html>
```